Company or website name
- Bright Hollow Properties
- Describe your company and organization and target audience
- We sell rural vacant, mostly residential land. Our target market is looking for privacy and either a place to retire to or a place to escape to.
- The design should have the following
- Mountains, Pine Trees, Earthy Colors, and match the attached logo. The home page should have designs for slides of properties at the top, followed by a survey (for users to share details of the property they're looking for), followed by search functionality, individual properties and general areas properties are available in. We'll also need at least one contact form on each page as well as maps. For the property detail page we'll need a large area for pictures, highlighted property details, a description and more detailed facts about property. The property detail page should also have a survey for users to share details of what they're looking for and contact form. Last but not least, similar properties should also be included on the property listing page. The winning design will include an excellent "Contact Us" page! Every page should have an opt-in offering users to be notified when new properties become available.
- Briefly describe your contest

```html
<!DOCTYPE html>
<html lang="en">
<head>
<meta charset="utf-8">
<title>Bright Hollow Properties – Website Pages</title>
<link rel="stylesheet" href="https://fonts.googleapis.com/css2?family=Libre+Baskerville:ital,wght@0,400;0,700;1,400&family=Open+Sans:wght@400;600;700&display=swap">
<style>
:root{
  --green:#17624f;
  --green-dark:#0c4a38;
  --green-field:#0f4f3e;
  --page:#f2f2f2;
  --white:#ffffff;
  --ink:#333333;
  --accent:#3aa0c8;
  --title:#1d6b55;
}
*{box-sizing:border-box;margin:0;padding:0}
html,body{width:1200px;height:2229px;overflow:hidden;background:var(--white)}
body{font-family:"Open Sans",Arial,sans-serif;color:var(--ink)}
.board{position:absolute;left:0;top:0;width:1395px;height:2592px;transform:scale(.8602);transform-origin:0 0;background:var(--white)}
.abs{position:absolute}
.board-title{position:absolute;font-family:"Libre Baskerville",Georgia,serif;color:var(--title);font-size:22px;letter-spacing:6px;text-align:center;width:568px}
.page{position:absolute;background:var(--page);overflow:hidden;box-shadow:0 0 4px rgba(0,0,0,.25)}
.serif{font-family:"Libre Baskerville",Georgia,serif}

.brand{position:absolute;display:flex;align-items:center;gap:4px}
.brand-dot{width:22px;height:22px;border-radius:50%;background:var(--green-dark)}
.brand-name{font-size:6px;font-weight:700;color:var(--green-dark);line-height:1.1;width:40px}

.nav{position:absolute;left:0;right:0;background:#f7f7f7}
.nav-menu{position:absolute;display:flex;align-items:center;font-size:6px;letter-spacing:.4px;color:#444}
.nav-menu .active{color:var(--green)}
.nav-menu.home .active{color:var(--accent)}

.photo{position:absolute}
.ph-lake{background:linear-gradient(180deg,#6a7370 0%,#4a5651 35%,#2c3d36 62%,#1f2e29 80%,#3a3127 100%)}
.ph-blur{background:linear-gradient(180deg,#4b5451 0%,#5c6663 40%,#3b5a52 70%,#6b6a5c 100%)}
.ph-house1{background:linear-gradient(180deg,#8fb3d6 0%,#b9c7c7 45%,#6f8a52 80%,#4d6a35 100%)}
.ph-house2{background:linear-gradient(180deg,#5c7a3e 0%,#7f9a5a 50%,#4d6b34 100%)}
.ph-house3{background:linear-gradient(180deg,#9bbbe0 0%,#a5b2b2 45%,#8a5a48 70%,#5f7c3e 100%)}
.ph-lakehouse{background:linear-gradient(180deg,#aeb9bb 0%,#6d7f74 45%,#2f5a56 75%,#4a3a2c 100%)}
.ph-porch{background:linear-gradient(180deg,#3c5a36 0%,#86a4a8 50%,#dfe4e4 75%,#5a6e45 100%)}
.ph-forest{background:linear-gradient(180deg,#2d4a2c 0%,#3f5f34 55%,#c9d0d0 75%,#3a5630 100%)}
.ph-snow{background:linear-gradient(180deg,#3f4b57 0%,#2e3e3a 50%,#b97a44 72%,#d6dde0 100%)}
.ph-person{background:linear-gradient(180deg,#c9c9c9,#8d8d8d)}
.ph-map{background:
  radial-gradient(ellipse 60px 30px at 62% 70%,#cfe5c9 0%,rgba(207,229,201,0) 100%),
  radial-gradient(ellipse 50px 25px at 25% 60%,#d3e8cc 0%,rgba(211,232,204,0) 100%),
  radial-gradient(ellipse 90px 60px at 0% 0%,#f3d98a 0%,rgba(243,217,138,0) 100%),
  radial-gradient(ellipse 110px 70px at 100% 20%,#f5dc92 0%,rgba(245,220,146,0) 100%),
  radial-gradient(ellipse 70px 40px at 88% 50%,#d9dbe6 0%,rgba(217,219,230,0) 100%),
  linear-gradient(135deg,#eceee9 0%,#e7ebe4 50%,#ecebe4 100%)}

.btn-pill{position:absolute;background:var(--green-dark);color:#fff;border-radius:12px;font-size:8px;font-weight:700;letter-spacing:1.5px;text-align:center}
.btn-outline{position:absolute;border:1px solid var(--green);color:var(--green);font-size:9px;text-align:center}
.btn-light{position:absolute;border:1px solid #fff;color:#fff;font-size:9px;text-align:center}

.card{position:absolute;background:#fff;box-shadow:0 0 3px rgba(0,0,0,.15);overflow:hidden}
.feat-body{position:absolute;left:0;right:0;text-align:center;font-size:7px;color:#444;line-height:1.45}
.feat-name{font-size:9px;letter-spacing:.4px;margin-top:6px;line-height:1.55}
.blog-body{position:absolute;left:5px;right:5px;font-size:5px;color:#777;line-height:1.8;text-align:justify}
.blog-body .date{color:#999}
.blog-body h4{font-size:7px;color:#333;font-weight:600;letter-spacing:.4px;line-height:1.55;margin:4px 0 3px}

.footer{position:absolute;left:0;width:568px;background:var(--green);color:#fff}
.footer h5{position:absolute;font-size:4px;letter-spacing:.8px;font-weight:600}
.footer ul{position:absolute;list-style:none;font-size:3.6px;line-height:2.9}
.footer .info{position:absolute;font-size:3.6px;line-height:1.9}
.f-field{position:absolute;left:348px;width:109px;background:var(--green-field);border-bottom:1px solid #3a7d6b;font-size:3.4px;padding:3px}
.f-send{position:absolute;left:348px;width:47px;height:12px;border:1px solid #fff;font-size:3.6px;letter-spacing:.8px;text-align:center;line-height:10px}
.copyright{position:absolute;left:0;width:568px;height:17px;background:var(--green-dark);color:#fff;font-size:3.6px;text-align:center;line-height:17px}
.footer-wide{transform:scale(1.266);transform-origin:0 0}

.form-card{position:absolute;background:#fff;box-shadow:0 0 3px rgba(0,0,0,.2)}
.form-line{position:absolute;left:16px;right:16px;border-bottom:1px solid #ccc;font-size:3.5px;color:#999}
.info-card{position:absolute;left:348px;width:109px;background:#fff;box-shadow:0 0 3px rgba(0,0,0,.2);font-size:3.8px;padding:8px 7px;line-height:1.7}
.dot-ic{display:inline-block;width:5px;height:5px;border-radius:50%;background:#6ab04c;vertical-align:middle;margin-right:2px}

.side{position:absolute;left:111px;font-size:4px;color:#555;line-height:2.6}
.side h6{font-size:4.6px;letter-spacing:.6px;color:#333;font-weight:700}
.side hr{border:0;border-top:1px solid #bbb;width:14px;margin:1px 0}
.prop-text{position:absolute;font-size:3.8px;color:#555;line-height:1.8}
.prop-text .t{color:#333}
.prop-text .p{color:var(--green);font-weight:600}
.pager{position:absolute;display:flex;gap:9px;font-size:4px;color:#666;align-items:center}
.pager .cur{width:10px;height:10px;border:1px solid #666;border-radius:50%;text-align:center;line-height:8px}
</style>
</head>
<body>
<div class="board">

  <!-- HOMEPAGE -->
  <div class="board-title" style="left:109px;top:32px">HOMEPAGE</div>
  <section class="page" style="left:33px;top:87px;width:719px;height:1615px">
    <div class="abs" style="left:0;top:0;width:719px;height:22px;background:var(--green);color:#fff;font-size:5px">
      <span class="abs" style="left:22px;top:8px">✉ info@brighthollowproperties.com &nbsp;&nbsp;&nbsp; ☎ +1 555 204 7781</span>
      <span class="abs" style="right:22px;top:8px">Login &nbsp;/&nbsp; Signup</span>
    </div>
    <div class="nav" style="top:22px;height:38px">
      <div class="brand" style="left:20px;top:7px"><div class="brand-dot"></div><div class="brand-name">Bright Hollow</div></div>
      <div class="nav-menu home" style="right:24px;top:15px;gap:26px;font-size:6.5px">
        <span class="active">HOME</span><span>PROPERTIES</span><span>ABOUT US</span><span>CONTACT</span><span>BLOG</span>
        <svg width="10" height="10" viewBox="0 0 10 10"><circle cx="4" cy="4" r="3.2" fill="none" stroke="#333"/><line x1="6.4" y1="6.4" x2="9.2" y2="9.2" stroke="#333"/></svg>
      </div>
    </div>
    <div class="photo ph-lake" role="img" aria-label="Mountain lake with pine forest and a wooden boathouse" style="left:0;top:60px;width:719px;height:344px"></div>
    <h1 class="abs serif" style="left:0;width:719px;top:171px;text-align:center;color:#fff;font-size:16px;font-weight:400;letter-spacing:4px">WHAT ARE YOU LOOKING FOR?</h1>
    <p class="abs" style="left:0;width:719px;top:194px;text-align:center;color:#fff;font-size:6.5px">No matter what your property needs, Bright Hollow Properties is here for you</p>
    <div class="abs" style="left:201px;top:224px;width:74px;height:25px;background:#fff;border-radius:2px;font-size:8px;color:#888;padding:7px 5px">Buy / Sell<svg class="abs" style="right:5px;top:10px" width="9" height="5"><polyline points="0,0 4.5,4.5 9,0" fill="none" stroke="#666"/></svg></div>
    <div class="abs" style="left:285px;top:224px;width:112px;height:25px;background:#fff;border-radius:2px;font-size:8px;color:#888;padding:7px 6px">Neighborhood<svg class="abs" style="right:6px;top:10px" width="9" height="5"><polyline points="0,0 4.5,4.5 9,0" fill="none" stroke="#666"/></svg></div>
    <div class="abs" style="left:407px;top:224px;width:111px;height:25px;background:#fff;border-radius:2px;font-size:8px;color:#aaa;padding:7px 6px">$ Min<span class="abs" style="left:55px;top:7px;border-left:1px solid #ddd;padding-left:5px">$ Max</span></div>
    <div class="abs" style="left:201px;top:258px;width:317px;height:28px;background:#fff;border-radius:2px;font-size:8px;color:#999;padding:9px 6px">Enter an address, neigborhood, city or ZIP code
      <svg class="abs" style="right:8px;top:6px" width="15" height="15" viewBox="0 0 15 15"><circle cx="6.5" cy="6.5" r="5" fill="none" stroke="var(--green)" stroke-width="1.4"/><line x1="10" y1="10" x2="14" y2="14" stroke="var(--green)" stroke-width="1.4"/></svg>
    </div>
    <svg class="abs" style="left:330px;top:384px" width="50" height="8"><circle cx="10" cy="4" r="1.5" fill="#fff"/><rect x="27" y="1.5" width="4" height="4" fill="none" stroke="#fff" transform="rotate(45 29 3.5)"/><rect x="46" y="1.5" width="4" height="4" fill="none" stroke="#fff" transform="rotate(45 48 3.5)"/></svg>

    <h2 class="abs serif" style="left:0;width:719px;top:429px;text-align:center;color:var(--title);font-size:16px;font-weight:400;letter-spacing:4px">FEATURED PROPERTIES</h2>
    <div class="card" style="left:140px;top:471px;width:139px;height:197px">
      <div class="photo ph-house1" role="img" aria-label="White farmhouse with porch and lawn" style="left:0;top:0;width:139px;height:93px"></div>
      <div class="feat-body" style="top:103px">Redwood Forest Estate<br>Detail infomation<div class="feat-name">REDWOOD,<br>BLUE RAY WAY</div></div>
      <div class="btn-pill" style="left:30px;top:168px;width:76px;height:17px;line-height:17px">READ MORE</div>
    </div>
    <div class="card" style="left:289px;top:471px;width:139px;height:197px">
      <div class="photo ph-house2" role="img" aria-label="Stone cottage covered in ivy with a red door" style="left:0;top:0;width:139px;height:93px"></div>
      <div class="feat-body" style="top:103px">Redwood Forest Estate<br>Detail infomation<div class="feat-name">REDWOOD,<br>BLUE RAY WAY</div></div>
      <div class="btn-pill" style="left:30px;top:168px;width:76px;height:17px;line-height:17px">READ MORE</div>
    </div>
    <div class="card" style="left:438px;top:471px;width:139px;height:197px">
      <div class="photo ph-house3" role="img" aria-label="Brick family house with gabled roof" style="left:0;top:0;width:139px;height:93px"></div>
      <div class="feat-body" style="top:103px">Redwood Forest Estate<br>Detail infomation<div class="feat-name">REDWOOD,<br>BLUE RAY WAY</div></div>
      <div class="btn-pill" style="left:30px;top:168px;width:76px;height:17px;line-height:17px">READ MORE</div>
    </div>
    <div class="btn-outline" style="left:309px;top:699px;width:100px;height:22px;line-height:20px">View our properties</div>

    <div class="abs" style="left:0;top:747px;width:719px;height:91px;background:var(--green);color:#fff">
      <div class="abs" style="left:141px;top:24px;font-size:11px;letter-spacing:1px">GET BRIGHT HOLLOW UPDATES:</div>
      <div class="abs" style="left:141px;top:47px;font-size:6.5px;line-height:1.7;width:190px;color:#dfe">For exclusive news and market updates sign up for our newsletter.</div>
      <div class="abs" style="left:365px;top:18px;width:213px;height:23px;background:var(--green-dark);font-size:8px;color:#9bb;padding:6px 7px;letter-spacing:.5px">Email</div>
      <div class="abs" style="left:365px;top:49px;width:213px;height:23px;border:1px solid #e8d9a0;font-size:9px;text-align:center;line-height:21px;letter-spacing:.5px">Get updates</div>
    </div>
    <div class="abs" style="left:0;top:838px;width:719px;height:237px;background:var(--green-dark);color:#fff">
      <h2 class="abs serif" style="left:0;width:719px;top:25px;text-align:center;font-size:14px;font-weight:400;letter-spacing:4px">TESTIMONIALS</h2>
      <div class="photo ph-person" role="img" aria-label="Portrait of a client" style="left:141px;top:57px;width:51px;height:51px;border:2px solid #fff"></div>
      <p class="abs serif" style="left:204px;top:57px;width:374px;font-size:5.8px;font-style:italic;line-height:1.9">“Lorem ipsum dolor sit amet, consectetur adipiscing elit. Aliquam vel quam nibh. Nunc erat leo, viverra at purus ac, tincidunt tempor enim. Pellentesque in condimentum dui. Donec pulvinar hendrerit mauris, in lacinia augue auctor at. Proin euismod purus justo, id dictum turpis lacinia eget. ”</p>
      <div class="abs" style="left:204px;top:96px;font-size:5.8px;font-weight:700">LENA MARSH</div>
      <div class="abs" style="left:204px;top:104px;font-size:5px">Designer</div>
      <div class="photo ph-person" role="img" aria-label="Portrait of a client" style="left:141px;top:122px;width:51px;height:51px;border:2px solid #fff"></div>
      <p class="abs serif" style="left:204px;top:122px;width:374px;font-size:5.8px;font-style:italic;line-height:1.9">“Lorem ipsum dolor sit amet, consectetur adipiscing elit. Aliquam vel quam nibh. Nunc erat leo, viverra at purus ac, tincidunt tempor enim. Pellentesque in condimentum dui.”</p>
      <div class="abs" style="left:204px;top:161px;font-size:5.8px;font-weight:700">OWEN HARLOW</div>
      <div class="abs" style="left:204px;top:169px;font-size:5px">CEO</div>
      <div class="btn-light" style="left:285px;top:190px;width:149px;height:22px;line-height:20px">Read more client testimonials</div>
    </div>

    <h2 class="abs serif" style="left:0;width:719px;top:1099px;text-align:center;color:var(--title);font-size:16px;font-weight:400;letter-spacing:3px">FROM OUR BLOG</h2>
    <div class="card" style="left:140px;top:1141px;width:139px;height:206px">
      <div class="photo ph-house1" role="img" aria-label="Large house with palm trees" style="left:0;top:0;width:139px;height:105px"></div>
      <div class="blog-body" style="top:111px"><div class="date">March 19, 2022</div><h4>Lorem ipsum dolor sit amet, consectetur adipiscing elit.</h4>Lorem ipsum dolor sit amet, consectetur adipiscing elit. Aliquam vel quam nibh. Nunc erat leo, viverra at purus ac, tincidunt tempor enim. Pellentesque in condimentum dui</div>
    </div>
    <div class="card" style="left:290px;top:1141px;width:138px;height:206px">
      <div class="photo ph-lakehouse" role="img" aria-label="Boathouse on a mountain lake" style="left:0;top:0;width:138px;height:105px"></div>
      <div class="blog-body" style="top:111px"><div class="date">March 19, 2022</div><h4>Nunc erat leo, viverra at purus ac, tincidunt tempor enim.</h4>Lorem ipsum dolor sit amet, consectetur adipiscing elit. Aliquam vel quam nibh. Nunc erat leo, viverra at purus ac, tincidunt tempor enim. Pellentesque in condimentum dui</div>
    </div>
    <div class="card" style="left:440px;top:1141px;width:139px;height:206px">
      <div class="photo ph-porch" role="img" aria-label="Porch of a white house with garden flowers" style="left:0;top:0;width:139px;height:105px"></div>
      <div class="blog-body" style="top:111px"><div class="date">March 19, 2022</div><h4>viverra at purus ac, tincidunt tempor enim dui.</h4>Lorem ipsum dolor sit amet, consectetur adipiscing elit. Aliquam vel quam nibh. Nunc erat leo, viverra at purus ac, tincidunt tempor enim. Pellentesque in condimentum dui</div>
    </div>
    <div class="btn-outline" style="left:308px;top:1373px;width:101px;height:22px;line-height:20px">Visit our blog</div>

    <div class="footer footer-wide" style="top:1423px;height:135px">
      <h5 style="left:111px;top:17px">SEARCH PROPERTY</h5>
      <ul style="left:111px;top:29px"><li>Home for sale in Indiana</li><li>Home for sale in Maine</li><li>Home for sale in Massachusetts</li><li>Home for sale in Montana</li><li>Home for sale in South Carolina</li></ul>
      <h5 style="left:229px;top:17px">CONTACT US</h5>
      <div class="info" style="left:229px;top:32px">Phone number: +1 555 204 7781<br>Email: info@brighthollowproperties.com<br>Address: 418 Cedar Run, Alder Falls</div>
      <h5 style="left:348px;top:17px">WE WOULD LOVE TO HEAR FROM YOU</h5>
      <div class="f-field" style="top:27px;height:15px">Name</div>
      <div class="f-field" style="top:44px;height:15px">Email</div>
      <div class="f-field" style="top:61px;height:31px">Message</div>
      <div class="f-send" style="top:102px;height:14px;line-height:12px">SEND</div>
    </div>
    <div class="copyright" style="top:1595px;width:719px;height:20px;line-height:20px;font-size:4.6px">Copyright © 2022 BrightHollowProperties- All Rights Reserved</div>
  </section>

  <!-- CONTACT PAGE -->
  <div class="board-title" style="left:792px;top:33px">CONTACT PAGE</div>
  <section class="page" style="left:792px;top:87px;width:568px;height:693px">
    <div class="nav" style="top:0;height:30px">
      <div class="brand" style="left:16px;top:4px"><div class="brand-dot"></div></div>
      <div class="nav-menu" style="right:20px;top:11px;gap:18px;font-size:4.6px"><span class="active">HOME</span><span>PROPERTIES</span><span>ABOUT US</span><span>CONTACT</span><span>BLOG</span>
        <svg width="8" height="8" viewBox="0 0 10 10"><circle cx="4" cy="4" r="3.2" fill="none" stroke="#333"/><line x1="6.4" y1="6.4" x2="9.2" y2="9.2" stroke="#333"/></svg></div>
    </div>
    <div class="photo ph-blur" role="img" aria-label="Blurred mountain lake with boathouse" style="left:0;top:30px;width:568px;height:147px"></div>
    <h2 class="abs serif" style="left:0;width:568px;top:89px;text-align:center;color:#fff;font-size:12px;font-weight:400;letter-spacing:1.5px">CONTACT US</h2>
    <p class="abs" style="left:0;width:568px;top:108px;text-align:center;color:#fff;font-size:4.4px">No matter what your property needs, Bright Hollow Properties is here for you</p>
    <div class="form-card" style="left:111px;top:207px;width:227px;height:175px">
      <div class="abs serif" style="left:16px;top:17px;font-size:4.4px;font-style:italic;font-weight:700">We would love to hear from you</div>
      <div class="form-line" style="top:40px;height:10px">Name</div>
      <div class="form-line" style="top:63px;height:10px">Email</div>
      <div class="form-line" style="top:86px;height:28px">Message</div>
      <div class="abs" style="left:16px;top:132px;width:56px;height:15px;border:1px solid #333;font-size:4px;letter-spacing:1px;font-weight:700;text-align:center;line-height:13px">SEND</div>
    </div>
    <div class="info-card" style="top:207px;height:34px"><span class="dot-ic"></span><b>Phone number</b><br>+1 555 204 7781</div>
    <div class="info-card" style="top:252px;height:34px"><span class="dot-ic" style="background:#3a8fd0"></span><b>Email</b><br>info@brighthollowproperties.com</div>
    <div class="info-card" style="top:296px;height:44px"><span class="dot-ic"></span><b>Address</b><br>418 Cedar Run, Alder Falls,<br>United States</div>
    <div class="info-card" style="top:351px;height:31px"><span class="abs" style="left:18px;top:11px;width:7px;height:7px;background:#3b5998"></span><span class="abs" style="left:29px;top:11px;width:7px;height:7px;background:#1da1f2"></span></div>
    <div class="photo ph-map" role="img" aria-label="Street map of the office neighborhood in Alder Falls" style="left:0;top:412px;width:568px;height:129px"></div>
    <div class="footer" style="top:541px;height:135px">
      <h5 style="left:111px;top:17px">SEARCH PROPERTY</h5>
      <ul style="left:111px;top:29px"><li>Home for sale in Indiana</li><li>Home for sale in Maine</li><li>Home for sale in Massachusetts</li><li>Home for sale in Montana</li><li>Home for sale in South Carolina</li></ul>
      <h5 style="left:229px;top:17px">CONTACT US</h5>
      <div class="info" style="left:229px;top:32px">Phone number: +1 555 204 7781<br>Email: info@brighthollowproperties.com<br>Address: 418 Cedar Run, Alder Falls</div>
      <h5 style="left:348px;top:17px">WE WOULD LOVE TO HEAR FROM YOU</h5>
      <div class="f-field" style="top:27px;height:15px">Name</div>
      <div class="f-field" style="top:44px;height:15px">Email</div>
      <div class="f-field" style="top:61px;height:31px">Message</div>
      <div class="f-send" style="top:102px">SEND</div>
    </div>
    <div class="copyright" style="top:676px">Copyright © 2022 BrightHollowProperties- All Rights Reserved</div>
  </section>

  <!-- PROPERTIES -->
  <div class="board-title" style="left:792px;top:824px">PROPERTIES</div>
  <section class="page" style="left:792px;top:893px;width:568px;height:660px">
    <div class="nav" style="top:0;height:30px">
      <div class="brand" style="left:16px;top:4px"><div class="brand-dot"></div></div>
      <div class="nav-menu" style="right:20px;top:11px;gap:18px;font-size:4.6px"><span>HOME</span><span>PROPERTIES</span><span>ABOUT US</span><span>CONTACT</span><span>BLOG</span>
        <svg width="8" height="8" viewBox="0 0 10 10"><circle cx="4" cy="4" r="3.2" fill="none" stroke="#333"/><line x1="6.4" y1="6.4" x2="9.2" y2="9.2" stroke="#333"/></svg></div>
    </div>
    <div class="side" style="top:43px"><h6>PROPERTIES TYPE</h6><hr>Single family<br>Condo<br>Loft<br>Townhom<br>Vacan land</div>
    <div class="side" style="top:121px"><h6>PRICE</h6><hr>Under $150.000<br>$150.000 - $250.000<br>$250.000 - $400.000<br>Above $400.000</div>
    <div class="abs" style="left:199px;top:47px;width:258px;height:20px;background:#fff;border:1px solid #ddd;font-size:3.8px;color:#999">
      <span class="abs" style="left:5px;top:7px">Neighborhood, Address, Zip...</span>
      <span class="abs" style="left:88px;top:7px">Min Price ⌄</span>
      <span class="abs" style="left:124px;top:7px">Max Price ⌄</span>
      <span class="abs" style="left:160px;top:7px">Property Type</span>
      <span class="abs" style="left:226px;top:7px">⌄</span>
      <svg class="abs" style="right:6px;top:5px" width="9" height="9" viewBox="0 0 10 10"><circle cx="4" cy="4" r="3.2" fill="none" stroke="var(--green)"/><line x1="6.4" y1="6.4" x2="9.2" y2="9.2" stroke="var(--green)"/></svg>
    </div>

    <div class="photo ph-house3" role="img" aria-label="Brick house with garage" style="left:199px;top:76px;width:81px;height:80px"></div>
    <div class="abs" style="left:199px;top:140px;width:81px;font-size:3.4px;color:#fff;text-align:center;line-height:1.5">1000 sqft, 2 bedrooms, large yard and garden.</div>
    <div class="photo ph-lakehouse" role="img" aria-label="Boathouse on a mountain lake" style="left:288px;top:76px;width:81px;height:80px"></div>
    <div class="photo ph-porch" role="img" aria-label="Porch of a white house with garden" style="left:377px;top:76px;width:80px;height:80px"></div>
    <div class="prop-text" style="left:199px;top:161px"><span class="t">Redwood forest estate</span><br>2493 Elk Street, Pine Ridge, Oregon<br><span class="p">$99.000</span></div>
    <div class="prop-text" style="left:288px;top:161px"><span class="t">Redwood forest estate</span><br>2493 Elk Street, Pine Ridge, Oregon<br><span class="p">$99.000</span></div>
    <div class="prop-text" style="left:377px;top:161px"><span class="t">Redwood forest estate</span><br>2493 Elk Street, Pine Ridge, Oregon<br><span class="p">$99.000</span></div>

    <div class="photo ph-house3" role="img" aria-label="Brick family house" style="left:199px;top:203px;width:81px;height:80px"></div>
    <div class="photo ph-house2" role="img" aria-label="Ivy covered cottage with red door" style="left:288px;top:203px;width:81px;height:80px"></div>
    <div class="photo ph-house1" role="img" aria-label="White farmhouse with porch" style="left:377px;top:203px;width:80px;height:80px"></div>
    <div class="prop-text" style="left:199px;top:288px"><span class="t">Redwood forest estate</span><br>2493 Elk Street, Pine Ridge, Oregon<br><span class="p">$99.000</span></div>
    <div class="prop-text" style="left:288px;top:288px"><span class="t">Redwood forest estate</span><br>2493 Elk Street, Pine Ridge, Oregon<br><span class="p">$99.000</span></div>
    <div class="prop-text" style="left:377px;top:288px"><span class="t">Redwood forest estate</span><br>2493 Elk Street, Pine Ridge, Oregon<br><span class="p">$99.000</span></div>

    <div class="photo ph-forest" role="img" aria-label="House among tall pine trees" style="left:199px;top:330px;width:81px;height:80px"></div>
    <div class="photo ph-snow" role="img" aria-label="Lit cabin in a snowy pine forest" style="left:288px;top:330px;width:81px;height:80px"></div>
    <div class="photo ph-lakehouse" role="img" aria-label="Boathouse on a mountain lake" style="left:377px;top:330px;width:80px;height:80px"></div>
    <div class="prop-text" style="left:199px;top:415px"><span class="t">Redwood forest estate</span><br>2493 Elk Street, Pine Ridge, Oregon<br><span class="p">$99.000</span></div>
    <div class="prop-text" style="left:288px;top:415px"><span class="t">Redwood forest estate</span><br>2493 Elk Street, Pine Ridge, Oregon<br><span class="p">$99.000</span></div>
    <div class="prop-text" style="left:377px;top:415px"><span class="t">Redwood forest estate</span><br>2493 Elk Street, Pine Ridge, Oregon<br><span class="p">$99.000</span></div>
    <div class="abs" style="left:199px;top:457px;width:258px;border-top:1px solid #ddd"></div>
    <div class="pager" style="left:304px;top:468px"><span class="cur">1</span><span>2</span><span>3</span><span>›</span></div>

    <div class="footer" style="top:509px;height:135px">
      <h5 style="left:111px;top:17px">SEARCH PROPERTY</h5>
      <ul style="left:111px;top:29px"><li>Home for sale in Indiana</li><li>Home for sale in Maine</li><li>Home for sale in Massachusetts</li><li>Home for sale in Montana</li><li>Home for sale in South Carolina</li></ul>
      <h5 style="left:229px;top:17px">CONTACT US</h5>
      <div class="info" style="left:229px;top:32px">Phone number: +1 555 204 7781<br>Email: info@brighthollowproperties.com<br>Address: 418 Cedar Run, Alder Falls</div>
      <h5 style="left:348px;top:17px">WE WOULD LOVE TO HEAR FROM YOU</h5>
      <div class="f-field" style="top:27px;height:15px">Name</div>
      <div class="f-field" style="top:44px;height:15px">Email</div>
      <div class="f-field" style="top:61px;height:31px">Message</div>
      <div class="f-send" style="top:102px">SEND</div>
    </div>
    <div class="copyright" style="top:643px">Copyright © 2022 BrightHollowProperties- All Rights Reserved</div>
  </section>

  <!-- BLOG PAGE -->
  <div class="board-title" style="left:792px;top:1597px">BLOG PAGE</div>
  <section class="page" style="left:792px;top:1635px;width:568px;height:908px">
    <div class="nav" style="top:0;height:30px">
      <div class="brand" style="left:16px;top:4px"><div class="brand-dot"></div></div>
      <div class="nav-menu" style="right:20px;top:11px;gap:18px;font-size:4.6px"><span class="active">HOME</span><span>PROPERTIES</span><span>ABOUT US</span><span>CONTACT</span><span>BLOG</span>
        <svg width="8" height="8" viewBox="0 0 10 10"><circle cx="4" cy="4" r="3.2" fill="none" stroke="#333"/><line x1="6.4" y1="6.4" x2="9.2" y2="9.2" stroke="#333"/></svg></div>
    </div>
    <div class="photo ph-blur" role="img" aria-label="Blurred mountain lake with boathouse" style="left:0;top:30px;width:568px;height:147px"></div>
    <h2 class="abs serif" style="left:0;width:568px;top:96px;text-align:center;color:#fff;font-size:12px;font-weight:400;letter-spacing:1.5px">WELCOME TO OUR BLOG</h2>

    <div class="card" style="left:113px;top:207px;width:110px;height:153px"><div class="photo ph-lakehouse" role="img" aria-label="Boathouse on a mountain lake" style="left:0;top:0;width:110px;height:82px"></div><div class="blog-body" style="top:88px;font-size:3.6px;line-height:1.7"><div class="date">March 19, 2022</div><h4 style="font-size:4.8px">Bright Hollow Properties launching new website</h4>Lorem ipsum dolor sit amet, consectetur adipiscing elit, sed do eiusmod tempor incididunt ut labore et dolore...</div></div>
    <div class="card" style="left:231px;top:207px;width:110px;height:153px"><div class="photo ph-house3" role="img" aria-label="Brick house with garage" style="left:0;top:0;width:110px;height:82px"></div><div class="blog-body" style="top:88px;font-size:3.6px;line-height:1.7"><div class="date">March 19, 2022</div><h4 style="font-size:4.8px">Bright Hollow Properties launching new website</h4>Lorem ipsum dolor sit amet, consectetur adipiscing elit, sed do eiusmod tempor incididunt ut labore et dolore...</div></div>
    <div class="card" style="left:349px;top:207px;width:110px;height:153px"><div class="photo ph-porch" role="img" aria-label="Porch of a white house with flowers" style="left:0;top:0;width:110px;height:82px"></div><div class="blog-body" style="top:88px;font-size:3.6px;line-height:1.7"><div class="date">March 19, 2022</div><h4 style="font-size:4.8px">Bright Hollow Properties launching new website</h4>Lorem ipsum dolor sit amet, consectetur adipiscing elit, sed do eiusmod tempor incididunt ut labore et dolore...</div></div>
    <div class="card" style="left:113px;top:376px;width:110px;height:153px"><div class="photo ph-house1" role="img" aria-label="Large house with palm trees" style="left:0;top:0;width:110px;height:82px"></div><div class="blog-body" style="top:88px;font-size:3.6px;line-height:1.7"><div class="date">March 19, 2022</div><h4 style="font-size:4.8px">Bright Hollow Properties launching new website</h4>The responsive design revolution is truly upon us (if it hasn't already happened), and even</div></div>
    <div class="card" style="left:231px;top:376px;width:110px;height:153px"><div class="photo ph-house3" role="img" aria-label="Brick family house" style="left:0;top:0;width:110px;height:82px"></div><div class="blog-body" style="top:88px;font-size:3.6px;line-height:1.7"><div class="date">March 19, 2022</div><h4 style="font-size:4.8px">Bright Hollow Properties launching new website</h4>The responsive design revolution is truly upon us (if it hasn't already happened), and even</div></div>
    <div class="card" style="left:349px;top:376px;width:110px;height:153px"><div class="photo ph-house2" role="img" aria-label="Ivy covered cottage with red door" style="left:0;top:0;width:110px;height:82px"></div><div class="blog-body" style="top:88px;font-size:3.6px;line-height:1.7"><div class="date">March 19, 2022</div><h4 style="font-size:4.8px">Bright Hollow Properties launching new website</h4>The responsive design revolution is truly upon us (if it hasn't already happened), and even</div></div>
    <div class="card" style="left:113px;top:545px;width:110px;height:153px"><div class="photo ph-house1" role="img" aria-label="White farmhouse with porch" style="left:0;top:0;width:110px;height:82px"></div><div class="blog-body" style="top:88px;font-size:3.6px;line-height:1.7"><div class="date">March 19, 2022</div><h4 style="font-size:4.8px">Bright Hollow Properties launching new website</h4>The responsive design revolution is truly upon us (if it hasn't already happened), and even</div></div>
    <div class="card" style="left:231px;top:545px;width:110px;height:153px"><div class="photo ph-forest" role="img" aria-label="House among tall pine trees" style="left:0;top:0;width:110px;height:82px"></div><div class="blog-body" style="top:88px;font-size:3.6px;line-height:1.7"><div class="date">March 19, 2022</div><h4 style="font-size:4.8px">Bright Hollow Properties launching new website</h4>The responsive design revolution is truly upon us (if it hasn't already happened), and even</div></div>
    <div class="card" style="left:349px;top:545px;width:110px;height:153px"><div class="photo ph-snow" role="img" aria-label="Lit cabin in a snowy pine forest" style="left:0;top:0;width:110px;height:82px"></div><div class="blog-body" style="top:88px;font-size:3.6px;line-height:1.7"><div class="date">March 19, 2022</div><h4 style="font-size:4.8px">Bright Hollow Properties launching new website</h4>The responsive design revolution is truly upon us (if it hasn't already happened), and even</div></div>
    <div class="pager" style="left:232px;top:715px"><span style="margin-right:12px">‹</span><span class="cur">1</span><span>2</span><span>3</span><span>4</span><span style="margin-left:12px">›</span></div>

    <div class="footer" style="top:757px;height:134px">
      <h5 style="left:111px;top:17px">SEARCH PROPERTY</h5>
      <ul style="left:111px;top:29px"><li>Home for sale in Indiana</li><li>Home for sale in Maine</li><li>Home for sale in Massachusetts</li><li>Home for sale in Montana</li><li>Home for sale in South Carolina</li></ul>
      <h5 style="left:229px;top:17px">CONTACT US</h5>
      <div class="info" style="left:229px;top:32px">Phone number: +1 555 204 7781<br>Email: info@brighthollowproperties.com<br>Address: 418 Cedar Run, Alder Falls</div>
      <h5 style="left:348px;top:17px">WE WOULD LOVE TO HEAR FROM YOU</h5>
      <div class="f-field" style="top:27px;height:15px">Name</div>
      <div class="f-field" style="top:44px;height:15px">Email</div>
      <div class="f-field" style="top:61px;height:31px">Message</div>
      <div class="f-send" style="top:102px">SEND</div>
    </div>
    <div class="copyright" style="top:891px">Copyright © 2022 BrightHollowProperties- All Rights Reserved</div>
  </section>

</div>
</body>
</html>
```